Design a IronFlow Flyer to attract new membership

With constantly updating workouts and the nutritional help Tollmere Ironworks is more than just an average gym. It’s a place for everyone to get healthy in a stress-free, safe and friendly environment.

Target Market(s)

Women ages 25-60 years old

Industry/Entity Type

Environment

Font styles to use
Serif

Requirements
Must have
• Please read thru the following info before you begin your design:
• IronFlow Flyer Information
• Please keep in mind a few things:
• 1) Our facility colors orange and green (you can see from my website what the color scheme is)
• 2) Our target demo graphic is women between the ages of 25-60, a large majority of my current clientele are middle aged women 45-60 years old
• 3) Try to keep it clean, and white (like quills website) if possible
• Side 1: (image of equipment and a younger women working out)
• 1) TMIW Logo
• 2) FREE WEEK TRIAL (big font) Sing up at www.tmironworks.net/schedulesign-up
• 3) Schedule: Monday-Friday 5:30am – 6:15am – 6:00pm – 7:00pm
• 4) Rates: $150/ Month Unlimited Classes - $100 /10 session package
• *15% discount for all fire, police, military, veterans, teachers, current students & trade association members
• 5) Address: 217 Pell Avenue Staten Island, NY 10308
• 6) Contact info: Phone: 347-518-7064 Email: tmironworks@mailbox.example
• 7) Website and Social media www.tmironworks.net find us @TMIronworks on Facebook, Twitter, Instagram, Yelp, Google + and foursquare
• Side 2 (image of a women working out, preferable middle aged):
• 1) 6 Benefits of IronFlow:
• a. Benefit #1: It BLASTS calories
• b. Benefit #2: It’s great Cardiovascular conditioning
• c. Benefit #3: It increases joint mobility
• d. Benefit #4: Everyday is something different, guaranteed
• e. Benefit #5: You’ll make new friends
• f. Benefit #6: You’ll feel like a badass
• 2) Free Week Trial Class (smaller font at the bottom) sign up at: www.tmironworks.net/schedulesign-up

```html
<!DOCTYPE html>
<html lang="en">
<head>
<meta charset="utf-8">
<title>Tollmere Ironworks – Free Week Trial</title>
<link rel="stylesheet" href="https://fonts.googleapis.com/css2?family=Open+Sans:wght@400;600;700;800&display=swap">
<style>
  :root {
    --orange: #f3a50a;
    --green-dark: #16463a;
    --green-text: #1b4536;
    --white: #ffffff;
    --paper: #fdfdfd;
    --teal: #0f6b62;
    --shadow: rgba(0, 0, 0, 0.35);
  }
  * { margin: 0; padding: 0; box-sizing: border-box; }
  html, body { width: 846px; height: 1200px; overflow: hidden; background: var(--white); }
  body { font-family: "Open Sans", Arial, sans-serif; }

  .flyer { position: relative; width: 846px; height: 1200px; background: var(--paper); overflow: hidden; }

  .headline {
    position: absolute; top: 66px; left: 0; width: 846px; text-align: center;
    color: var(--orange); font-weight: 800; font-size: 51px; letter-spacing: -1px;
    text-shadow: 1px 2px 2px rgba(0,0,0,0.15);
  }

  .athlete-photo { position: absolute; left: 0; top: 148px; width: 472px; height: 535px; }

  .benefit {
    position: absolute; display: flex; align-items: flex-start; gap: 8px;
    color: var(--green-text); font-weight: 700; text-transform: uppercase;
    text-shadow: 1px 1px 1px rgba(0,0,0,0.15);
  }
  .benefit .num { font-size: 35px; font-weight: 800; line-height: 1; }
  .benefit .text { font-size: 19px; line-height: 28px; padding-top: 6px; letter-spacing: -0.2px; }
  .b1 { left: 440px; top: 196px; }
  .b2 { left: 472px; top: 258px; }
  .b3 { left: 488px; top: 352px; }
  .b4 { left: 486px; top: 420px; }
  .b5 { left: 472px; top: 510px; }
  .b6 { left: 436px; top: 588px; }

  .offer-band { position: absolute; left: 0; top: 683px; width: 846px; height: 436px; background: var(--green-dark); }

  .brand-mark {
    position: absolute; left: 25px; top: 40px; width: 173px; height: 173px;
    border: 3px solid var(--white); background: var(--teal);
    display: flex; align-items: center; justify-content: center; text-align: center;
  }
  .brand-name { color: var(--white); font-weight: 700; font-size: 20px; line-height: 1.2; text-transform: uppercase; }

  .trial-small {
    position: absolute; left: 262px; top: 40px; color: var(--white);
    font-weight: 800; font-size: 60px; letter-spacing: -2px; line-height: 1;
    text-shadow: 3px 3px 3px var(--shadow);
  }
  .trial-big {
    position: absolute; left: 248px; top: 100px; color: var(--orange);
    font-weight: 800; font-size: 132px; letter-spacing: -3px; line-height: 1;
    text-shadow: 4px 4px 4px var(--shadow);
  }

  .signup {
    position: absolute; left: 0; top: 250px; width: 846px; text-align: center;
    color: var(--white); font-size: 29px; line-height: 46px;
  }

  .social {
    position: absolute; left: 148px; top: 365px; display: flex; align-items: center; gap: 9px;
    color: var(--white); font-size: 18px;
  }
  .social .handle { font-weight: 700; }
  .social .label { margin-right: 8px; }
  .social-dot { width: 38px; height: 38px; border-radius: 50%; background: #3d6fb0; }
  .social-dot.alt { background: #c23a2b; }

  .footer-band {
    position: absolute; left: 0; top: 1119px; width: 846px; height: 81px; background: var(--orange);
    color: var(--white); font-size: 22px; text-align: center; line-height: 78px;
  }
</style>
</head>
<body>
<main class="flyer">
  <h1 class="headline">6 BENEFITS OF IRONFLOW</h1>

  <svg class="athlete-photo" viewBox="0 0 472 535" role="img" aria-label="Photo of a young woman in a black tank top curling a hexagonal dumbbell">
    <defs>
      <linearGradient id="athleteTone" x1="0" y1="0" x2="0" y2="1">
        <stop offset="0" stop-color="#fdfdfd"/>
        <stop offset="0.25" stop-color="#e9cdb4"/>
        <stop offset="0.55" stop-color="#d8b79c"/>
        <stop offset="0.75" stop-color="#2a2a2a"/>
        <stop offset="1" stop-color="#121212"/>
      </linearGradient>
    </defs>
    <rect width="472" height="535" fill="url(#athleteTone)"/>
  </svg>

  <div class="benefit b1"><span class="num">1.</span><span class="text">It blasts calories</span></div>
  <div class="benefit b2"><span class="num">2.</span><span class="text">It’s great cardiovascular<br>conditioning</span></div>
  <div class="benefit b3"><span class="num">3.</span><span class="text">It increases joint mobility</span></div>
  <div class="benefit b4"><span class="num">4.</span><span class="text">Everyday is something dif<br>ferent, guaranteed</span></div>
  <div class="benefit b5"><span class="num">5.</span><span class="text">You’ll make new friends</span></div>
  <div class="benefit b6"><span class="num">6.</span><span class="text">You’ll feel like a badass</span></div>

  <section class="offer-band">
    <div class="brand-mark"><span class="brand-name">Tollmere<br>Ironworks</span></div>
    <div class="trial-small">FREE WEEK</div>
    <div class="trial-big">TRIAL</div>
    <p class="signup">Sing up at<br>www.tmironworks.net/schedulesign-up</p>
    <div class="social">
      <span class="label">Find us @ <span class="handle">TMIronworks</span> on</span>
      <span class="social-dot"></span>
      <span class="social-dot"></span>
      <span class="social-dot"></span>
      <span class="social-dot alt"></span>
      <span class="social-dot alt"></span>
      <span class="social-dot"></span>
    </div>
  </section>

  <footer class="footer-band">www.tmironworks.net</footer>
</main>
</body>
</html>
```